依頼詳細
チラシデザインをお願いします。
初開催のため、写真がないので、イラストのみでの作成をお願いします。
地域の子どもたちに参加してもらいたいことから、子どもたちにも親しみやすい、柔らかいデザインを希望します。
記載項目
タイトル|きらきら星あかり祭
日時|2018年8月12日 18:00~
場所|道の駅ツバメの丘ほしの と 森沢町役場の芝生広場
・まわってごらん輪おどり(18:00~20:00)
道の駅に特設やぐらが登場するよ!
いつでもだれでも輪になって踊ろう!
・のぞいてごらん星空スクリーン(18:00~20:00)
役場の芝生広場が映画館になるよ
鑑賞無料
18:00~「三日月の約束」森沢町が舞台のラブストーリー
18:30~「ポコタンズ」
レジャーシートをもって寝そべってみよう!
・たべてごらん屋台村(18:00~20:30)
日没から営業開始!この日限定の屋台だよ
ヤキソバ、からあげ、フライドポテト、ジュース、ビール
地図|添付します
サイズ
A4
ページ数
片面
希望イメージ
• +5 0 +5
• シンプル
複雑
• 単色
カラフル
• 暗い
明るい
• 日常
高級
• 遊び心
厳粛
• 未来的
伝統的
• 女性的
男性的
希望する色
青系、紫系
納品ファイル
• イラストレーター形式 (.ai)
補足説明
地図と、イメージしているデザインに近いサンプルを添付します
依頼公開後の追記内容
作成していただいたチラシは印刷して配布する以外にも、HPやchatterbookでjpg形式で掲載させていただきますのでご了承ください。
チラシに下記を追記してください
主催者|道の駅ツバメの丘ほしの、森沢町観光協会
問い合わせ|0299-41-7720 または 0299-41-7722
応募くださったクリエイターのみなさまへ

たくさんの力作を制作いただきまことにありがとうございます!
みなさま甲乙つけがたいほどのクオリティで選択に困ってしまうほどです。
選考決定まで、どうか今しばらくおまちくださいませ。
■ 選んだ理由

やぐら、屋台、星空スクリーンのイラストがイメージ通りだった(位置までも!笑)
真ん中に配置された月が印象的で目を引いたし、私たちが描いてたイメージに一番近い作品だったので。

■ 提案者全員のお礼・コメント

みなさま力作ぞろいで、1点に絞るのは苦渋の決断でした。
応募いただいた作品を印刷して壁に張って、スタッフ総出で悩みながらの選出でした。
小さな町なので、そんなに頻繁にイベントはできませんが、また開催する際にはお願いしたいと思いますので、機会が合いましたらぜひよろしくおねがいします。

```html
<!DOCTYPE html>
<html lang="ja">
<head>
<meta charset="utf-8">
<title>きらきら星あかり祭</title>
<link rel="stylesheet" href="https://fonts.googleapis.com/css2?family=M+PLUS+Rounded+1c:wght@400;700;800;900&display=swap">
<style>
:root{
  --night:#1c2a5c;
  --night-deep:#141f48;
  --moon:#d4ebf7;
  --hill:#cfe5f4;
  --title:#fff4b8;
  --date:#ffe15a;
  --white:#ffffff;
  --pink:#f7c9d8;
  --pink-strong:#e2577f;
  --ink:#23305e;
  --badge:#e8465f;
}
*{margin:0;padding:0;box-sizing:border-box}
html,body{width:846px;height:1200px;overflow:hidden;background:var(--night)}
body{font-family:"M PLUS Rounded 1c",sans-serif;color:var(--ink)}
.flyer{position:relative;width:846px;height:1200px;overflow:hidden;
  background:linear-gradient(180deg,var(--night-deep) 0%,var(--night) 55%)}
.backdrop{position:absolute;inset:0}
.organizer{position:absolute;left:20px;top:18px;color:var(--white);font-size:13px;line-height:1.6;font-weight:700;
  display:grid;grid-template-columns:76px auto;column-gap:4px}
.organizer dt{white-space:nowrap}
.date{position:absolute;right:40px;top:16px;color:var(--date);font-weight:900;text-align:right}
.date .day{font-size:58px;letter-spacing:1px;line-height:1;white-space:nowrap}
.date .dow{display:inline-block;width:36px;height:36px;border-radius:50%;background:var(--date);color:var(--night);font-size:20px;line-height:36px;text-align:center;vertical-align:middle;margin-left:4px}
.date .time{font-size:32px;margin-top:6px;margin-right:6px}
.edition{position:absolute;top:145px;width:100%;text-align:center;color:var(--white);font-size:22px;font-weight:700;letter-spacing:2px}
.title{position:absolute;top:182px;width:100%;text-align:center;color:var(--title);font-weight:900;line-height:1.06;letter-spacing:4px;white-space:nowrap}
.title .l1{display:block;font-size:84px}
.title .l2{display:block;font-size:88px}
.venue{position:absolute;top:408px;width:100%;text-align:center;color:var(--ink);font-weight:800;font-size:23px;line-height:1.4}
.venue .tag{display:inline-block;background:var(--ink);color:var(--white);font-size:15px;padding:2px 14px;border-radius:14px;margin-bottom:4px}
.event{position:absolute;text-align:center;font-weight:700}
.event .name{font-weight:900;line-height:1.2}
.event .name .lead{display:block;font-size:22px}
.event .name .main{display:block;font-size:34px;white-space:nowrap}
.event .hours{font-size:21px;font-weight:800;margin:6px 0 8px}
.event .note{font-size:13.5px;line-height:1.55;font-weight:700;white-space:nowrap}
.dance{left:293px;top:560px;width:260px}
.dance .name{color:var(--pink-strong)}
.food{left:38px;top:730px;width:244px}
.screen{left:560px;top:755px;width:262px}
.screen .name .main{font-size:29px}
.screen .films{font-size:15px;font-weight:800;line-height:1.5;margin-bottom:4px}
.badge{position:absolute;left:758px;top:690px;width:74px;height:74px;border-radius:50%;background:var(--badge);color:var(--white);font-size:15px;font-weight:900;line-height:1.2;display:flex;align-items:center;justify-content:center;text-align:center}
</style>
</head>
<body>
<main class="flyer">
  <svg class="backdrop" width="846" height="1200" viewBox="0 0 846 1200">
    <defs>
      <radialGradient id="warm" cx="50%" cy="50%" r="50%"><stop offset="0" stop-color="#f0c08e" stop-opacity=".75"/><stop offset="1" stop-color="#f0c08e" stop-opacity="0"/></radialGradient>
      <radialGradient id="cool" cx="50%" cy="50%" r="50%"><stop offset="0" stop-color="#9dbfe2" stop-opacity=".8"/><stop offset="1" stop-color="#9dbfe2" stop-opacity="0"/></radialGradient>
      <radialGradient id="soft" cx="50%" cy="50%" r="50%"><stop offset="0" stop-color="#c9d6f0" stop-opacity=".6"/><stop offset="1" stop-color="#c9d6f0" stop-opacity="0"/></radialGradient>
      <linearGradient id="lantern" x1="0" x2="1"><stop offset="0" stop-color="#d8e4f6" stop-opacity=".45"/><stop offset="1" stop-color="#d8e4f6" stop-opacity=".1"/></linearGradient>
    </defs>
    <g class="stars" fill="#ffffff" opacity=".8">
      <circle cx="190" cy="60" r="2"/><circle cx="300" cy="110" r="1.6"/><circle cx="460" cy="40" r="2"/>
      <circle cx="560" cy="120" r="1.5"/><circle cx="240" cy="160" r="1.4"/><circle cx="620" cy="170" r="1.8"/>
      <circle cx="90" cy="150" r="1.6"/><circle cx="380" cy="70" r="1.3"/><circle cx="780" cy="160" r="1.5"/>
      <circle cx="60" cy="420" r="1.5"/><circle cx="800" cy="470" r="1.8"/><circle cx="30" cy="560" r="1.3"/>
    </g>
    <circle class="moon" cx="423" cy="440" r="215" fill="var(--moon)"/>
    <path class="hill" d="M0 640 Q 423 520 846 640 L846 1200 L0 1200 Z" fill="var(--hill)"/>
    <circle class="dance-disc" cx="423" cy="670" r="148" fill="var(--white)"/>
    <circle class="food-disc" cx="160" cy="840" r="145" fill="var(--pink)"/>
    <circle class="screen-disc" cx="692" cy="860" r="148" fill="var(--pink)"/>

    <ellipse role="img" aria-label="やきそば・からあげ・ポテトなど屋台の食べ物のイラスト" cx="95" cy="260" rx="85" ry="80" fill="url(#warm)"/>
    <ellipse role="img" aria-label="ビールジョッキと映写機のイラスト" cx="755" cy="270" rx="85" ry="85" fill="url(#soft)"/>
    <rect role="img" aria-label="夜空に連なる提灯の飾り" x="0" y="392" width="190" height="40" rx="20" fill="url(#lantern)"/>
    <rect role="img" aria-label="夜空に連なる提灯の飾り" x="656" y="392" width="190" height="40" rx="20" fill="url(#lantern)" transform="rotate(180 751 412)"/>
    <ellipse role="img" aria-label="紅白幕の特設やぐらのイラスト" cx="423" cy="386" rx="70" ry="14" fill="url(#warm)"/>
    <ellipse role="img" aria-label="浴衣で歩く親子のイラスト" cx="110" cy="545" rx="80" ry="80" fill="url(#cool)"/>
    <ellipse role="img" aria-label="手をふる子どものイラスト" cx="740" cy="575" rx="75" ry="75" fill="url(#cool)"/>
    <rect role="img" aria-label="道の駅と役場の芝生広場を示す会場地図" x="305" y="830" width="236" height="190" rx="14" fill="#ffffff" opacity=".7"/>
    <ellipse role="img" aria-label="屋台で食べる家族のイラスト" cx="155" cy="1095" rx="130" ry="85" fill="url(#warm)"/>
    <ellipse role="img" aria-label="芝生の上の星空スクリーンで映画を見る人々のイラスト" cx="690" cy="1105" rx="130" ry="80" fill="url(#cool)"/>
  </svg>

  <dl class="organizer">
    <dt>主　催</dt><dd>道の駅ツバメの丘ほしの<br>森沢町観光協会</dd>
    <dt>問い合わせ</dt><dd>0299-41-7720 または<br>0299-41-7722</dd>
  </dl>

  <div class="date">
    <div class="day">8/12<span class="dow">日</span></div>
    <div class="time">18:00〜</div>
  </div>

  <p class="edition">2018年 第1回</p>
  <h1 class="title"><span class="l1">きらきら</span><span class="l2">星あかり祭</span></h1>

  <div class="venue">
    <span class="tag">場所</span><br>
    道の駅ツバメの丘ほしの<br>森沢町役場の芝生広場
  </div>

  <section class="event dance">
    <h2 class="name"><span class="lead">まわってごらん</span><span class="main">輪おどり</span></h2>
    <p class="hours">18:00〜20:00</p>
    <p class="note">道の駅に特設やぐらが登場するよ！<br>いつでもだれでも<br>輪になって踊ろう！</p>
  </section>

  <section class="event food">
    <h2 class="name"><span class="lead">たべてごらん</span><span class="main">屋台村</span></h2>
    <p class="hours">18:00〜20:30</p>
    <p class="note">日没から営業開始！<br>この日限定の屋台だよ<br>ヤキソバ、からあげ、<br>フライドポテト、ジュース、ビール</p>
  </section>

  <section class="event screen">
    <h2 class="name"><span class="lead">のぞいてごらん</span><span class="main">星空スクリーン</span></h2>
    <p class="hours">18:00〜20:00</p>
    <p class="films">18:00〜「三日月の約束」<br>18:30〜「ポコタンズ」</p>
    <p class="note">役場の芝生広場が映画館になるよ<br>レジャーシートをもって<br>寝そべってみよう！</p>
  </section>
  <div class="badge">鑑賞<br>無料</div>
</main>
</body>
</html>
```